New Business Cards for Parvel

About Parvel:
At Parvel, we're more than just a company—we're a force for positive change in the staffing industry. Our brand is our heartbeat, and we need a designer who can translate that into every design element.

The Project:
We're revamping our business cards and need your artistic flair to make them stand out. Here's what we're looking for:

- Incorporate our existing brand elements (logo, colours, fonts) into the design.
- Craft a design that's sleek, professional, and memorable.
- Provide options for different layouts and finishes.
- Collaborate closely with our team to ensure the final product exceeds expectations.

Please note: For general text, we use Avenir. The brand guidelines are slightly out of date and don't have correct imaging. Colours are correct though.

```html
<!DOCTYPE html>
<html lang="en">
<head>
<meta charset="utf-8">
<title>Parvel Business Cards</title>
<link href="https://fonts.googleapis.com/css2?family=Nunito+Sans:wght@300;400;700;800&display=swap" rel="stylesheet">
<style>
  :root {
    --stage: #232323;
    --card-front: #211f25;
    --card-back: #141316;
    --brand-purple: #6d3d8e;
    --brand-pink: #e3197f;
    --plum: #5a2c4c;
    --violet-deep: #3d2b48;
    --text-light: #f2f0f4;
    --text-soft: #bdb6c4;
  }
  * { box-sizing: border-box; margin: 0; padding: 0; }
  html, body {
    width: 1200px; height: 780px; overflow: hidden;
    background: var(--stage);
    font-family: "Nunito Sans", "Avenir", sans-serif;
  }
  .sheet {
    width: 1200px; height: 780px;
    display: flex; align-items: center; justify-content: center; gap: 40px;
  }
  .card {
    position: relative;
    width: 540px; height: 330px;
    border-radius: 4px;
    overflow: hidden;
    box-shadow: 0 18px 40px rgba(0,0,0,0.45);
  }
  /* Front */
  .card--front { background: var(--card-front); }
  .brand {
    position: absolute; left: 150px; top: 34px;
    display: flex; flex-direction: column; align-items: flex-end;
  }
  .brand__name {
    font-weight: 700; font-size: 42px; line-height: 1;
    color: var(--text-light); letter-spacing: 0.5px;
  }
  .brand__tagline {
    font-size: 10px; font-weight: 400; color: var(--text-soft);
    margin-top: 6px;
  }
  .person {
    position: absolute; left: 28px; top: 112px;
    padding-left: 14px;
    border-left: 8px solid var(--brand-pink);
  }
  .person__name {
    font-weight: 800; font-size: 26px; line-height: 1;
    background: linear-gradient(90deg, var(--brand-pink) 0%, var(--brand-purple) 80%);
    -webkit-background-clip: text; background-clip: text; color: transparent;
  }
  .person__role {
    font-size: 13px; color: var(--text-light); font-weight: 400; margin-top: 2px;
  }
  .address {
    position: absolute; left: 60px; top: 168px;
    font-size: 13px; font-weight: 300; color: var(--text-light); line-height: 1.3;
  }
  .contacts {
    position: absolute; left: 36px; top: 212px;
    list-style: none;
    font-size: 13px; font-weight: 300; color: var(--text-light);
  }
  .contacts li { display: flex; align-items: center; gap: 10px; height: 22px; }
  .contacts svg { width: 13px; height: 13px; flex: none; }
  .emblem-area {
    position: absolute; right: -40px; bottom: -50px;
    width: 300px; height: 250px;
    border-radius: 48% 52% 40% 60% / 55% 45% 55% 45%;
    background: linear-gradient(135deg, var(--violet-deep) 0%, var(--plum) 60%, #4a2740 100%);
    opacity: 0.9;
  }
  /* Back */
  .card--back { background: var(--card-back); }
  .pattern-area {
    position: absolute; inset: 0;
    background: linear-gradient(120deg, #121114 0%, #1a191c 45%, #4a4a4e 75%, #9a9a9e 100%);
  }
  .back-brand {
    position: absolute; right: 70px; bottom: 40px;
    font-weight: 700; font-size: 20px; color: var(--text-light);
  }
</style>
</head>
<body>
<main class="sheet">
  <section class="card card--front" aria-label="Business card front">
    <div class="brand">
      <div class="brand__name">Parvel</div>
      <div class="brand__tagline">staffing with heart</div>
    </div>

    <div class="person">
      <h1 class="person__name">Marcus Hale</h1>
      <p class="person__role">CEO</p>
    </div>

    <p class="address">Riverton, 2450 NSW<br>Australia</p>

    <ul class="contacts">
      <li>
        <svg viewBox="0 0 14 14" aria-hidden="true"><rect x="3.5" y="1" width="7" height="12" rx="1.2" fill="none" stroke="#e3197f" stroke-width="1.3"/></svg>
        0491552803
      </li>
      <li>
        <svg viewBox="0 0 14 14" aria-hidden="true"><path d="M3 1.5l2.2 2.6-1.2 1.6c.9 1.8 2.3 3.2 4.1 4.1l1.6-1.2 2.6 2.2-1.3 1.7C6.4 12.3 1.7 7.6 1.5 2.8z" fill="#e3197f"/></svg>
        1300 718 245
      </li>
      <li>
        <svg viewBox="0 0 14 14" aria-hidden="true"><circle cx="7" cy="7" r="5.7" fill="none" stroke="#e3197f" stroke-width="1.3"/><path d="M1.5 7h11M7 1.3c-2.2 3.6-2.2 7.8 0 11.4M7 1.3c2.2 3.6 2.2 7.8 0 11.4" fill="none" stroke="#e3197f" stroke-width="1"/></svg>
        www.parvelcare.com.au
      </li>
      <li>
        <svg viewBox="0 0 14 14" aria-hidden="true"><rect x="1" y="3" width="12" height="8.5" rx="1" fill="#e3197f"/><path d="M1.5 3.6L7 8l5.5-4.4" fill="none" stroke="#211f25" stroke-width="1.1"/></svg>
        marcus.hale@parvelcare.com.au
      </li>
    </ul>

    <div class="emblem-area" role="img" aria-label="Large brand emblem decoration in purple and plum tones"></div>
  </section>

  <section class="card card--back" aria-label="Business card back">
    <div class="pattern-area" role="img" aria-label="Repeating brand emblem pattern with a glossy silver sheen"></div>
    <div class="back-brand">Parvel</div>
  </section>
</main>
</body>
</html>
```